Posters for Sociology/Inequality exhibition

I need about 10 similarly themed A2 sized posters (so you don't need to do each one from scratch) for a Sociology exhibition on Inequality. The first half are general descriptions about Sociology, the second half, about inequality. They are meant to be educational to a university student audience.

We are from the Lantern Society. I have attached a file below about the write-up content for the various posters, do have a look and do your sample base on that. The write-up is not yet complete, so it may change. Likewise, the point form of the write-up are for reading only, I don't expect them to be in the poster.

Feel free to separate the points if you find them too wordy, because I do not have an idea how the poster will eventually look like. Try your best!

-

Note: There were some problems with the word file attached, but I have changed and fixed it already, do have a look at it!

Also, I need the posters by Saturday/Sunday so most probably I will award the winner before that. I need it done earlier than later because I still need to get it approved.

The size may be big but that's because I want it to be readable, rather than have too many things in it.

You don't have to do all the 10 different ones first, just start with some or a few, submit a sample, and we'll take it from there!

Please ask if you have any questions!
Updates

Hi everyone, post your samples (1 or a few) soon because I will have a make a decision soon, most probably by tomorrow. 

I know it's rushed but try your best.

Target Market(s)

18-28 years old students at an institute/university

Industry/Entity Type

University

Requirements
Must have
• 1. A consistent theme that runs throughout the posters.
2. Very Readable, Appealing Font
3. Visually appealing for an exhibition
Should not have
• Not be too overwhelming

```html
<!DOCTYPE html>
<html lang="en">
<head>
<meta charset="utf-8">
<title>What is Sociology? — Introduction</title>
<link rel="stylesheet" href="https://fonts.googleapis.com/css2?family=Source+Sans+3:wght@400;600;700&display=swap">
<style>
  :root {
    --paper-top: #f8e9da;
    --paper-bottom: #fbf1e6;
    --coral: #e2574b;
    --coral-soft: #f08a72;
    --teal: #2a8a8c;
    --ink: #3a3a3a;
    --ink-soft: #5a5a5a;
    --label-dark: #3b2f2f;
    --card: #e9e4df;
    --card-edge: #d9d2cb;
  }
  * { box-sizing: border-box; margin: 0; padding: 0; }
  html, body { width: 900px; height: 1200px; overflow: hidden; }
  body {
    font-family: "Source Sans 3", Arial, sans-serif;
    color: var(--ink);
    background: #ffffff;
  }
  .poster {
    position: relative;
    width: 900px;
    height: 1200px;
    overflow: hidden;
    background: linear-gradient(180deg, var(--paper-top) 0%, var(--paper-bottom) 100%);
  }
  .header-scene {
    position: absolute; left: 0; top: 0; width: 900px; height: 215px;
    background: linear-gradient(180deg, #f3b79b 0%, var(--coral-soft) 45%, var(--coral) 100%);
  }
  .section-label {
    position: absolute; top: 28px; right: 36px;
    width: 250px; height: 38px;
    background: var(--label-dark);
    color: #fff; font-weight: 700; letter-spacing: 2px;
    font-size: 18px; line-height: 38px; text-align: center;
  }
  .section-title {
    position: absolute; left: 60px;
    display: flex; align-items: center; gap: 16px;
    font-size: 38px; font-weight: 700; color: var(--ink);
  }
  .section-title svg { width: 34px; height: 34px; flex: none; }
  .definitions { position: absolute; top: 330px; left: 70px; width: 760px; display: flex; justify-content: space-between; }
  .definition-card {
    position: relative; width: 200px; height: 240px;
    background: var(--card); border: 2px solid var(--card-edge);
    border-radius: 6px; padding: 48px 16px 16px;
    font-size: 20px; line-height: 1.3; text-align: center; color: var(--ink);
  }
  .definition-card .badge {
    position: absolute; top: -24px; left: 50%; transform: translateX(-50%);
    width: 48px; height: 48px; border-radius: 50%;
    background: var(--coral); border: 4px solid var(--paper-top);
  }
  .source-note { position: absolute; top: 590px; left: 72px; font-size: 14px; color: var(--ink-soft); }
  .birds {
    position: absolute; left: 470px; top: 560px; width: 420px; height: 190px;
    background: radial-gradient(ellipse at 60% 50%, rgba(58,47,47,0.18), rgba(58,47,47,0) 70%);
  }
  .practice-list { position: absolute; top: 712px; left: 72px; width: 560px; list-style: none; }
  .practice-list li {
    position: relative; padding-left: 36px; margin-bottom: 10px;
    font-size: 17px; line-height: 1.28; color: var(--ink);
  }
  .practice-list li svg { position: absolute; left: 0; top: 1px; width: 22px; height: 22px; }
  .brain-figure {
    position: absolute; left: 640px; top: 760px; width: 210px; height: 210px;
    border-radius: 50%;
    background: radial-gradient(circle, #fff6ee 0%, #f9e2d2 70%, rgba(249,226,210,0) 100%);
  }
  .study-intro { position: absolute; top: 1028px; left: 112px; font-size: 18px; color: var(--ink); }
  .study-line { position: absolute; left: 0; top: 1040px; }
  .topic {
    position: absolute; width: 140px; text-align: center;
    font-size: 15px; line-height: 1.1; color: var(--ink);
  }
  .topic.upper { top: 1077px; }
  .topic.lower { top: 1150px; }
</style>
</head>
<body>
<main class="poster">
  <div class="header-scene" role="img" aria-label="Coral illustrated skyline of city buildings, trees and turning gears"></div>
  <div class="section-label">INTRODUCTION</div>

  <h2 class="section-title" style="top:246px">
    <svg viewBox="0 0 34 34" aria-hidden="true"><path d="M3 4h28v20H14l-8 7v-7H3z" fill="var(--teal)"/></svg>
    What is Sociology?
  </h2>

  <section class="definitions">
    <div class="definition-card"><span class="badge"></span>Broadly speaking, Sociology is the study of society.</div>
    <div class="definition-card"><span class="badge"></span>It is a social science involving the study of the social lives of people, groups, and societies.</div>
    <div class="definition-card"><span class="badge"></span>An overarching unification of all the studies of humankind, including History, Psychology, and Economics.</div>
  </section>
  <p class="source-note">(from the Northbridge Sociological Association)</p>

  <div class="birds" role="img" aria-label="Flock of small birds scattering into the air"></div>

  <h2 class="section-title" style="top:636px">
    <svg viewBox="0 0 34 34" aria-hidden="true"><path d="M3 4h28v20H14l-8 7v-7H3z" fill="var(--teal)"/></svg>
    What do Sociologists do?
  </h2>

  <ul class="practice-list">
    <li><svg viewBox="0 0 22 22" aria-hidden="true"><circle cx="11" cy="11" r="7" fill="none" stroke="var(--coral)" stroke-width="4" stroke-dasharray="3 2.5"/><circle cx="11" cy="11" r="3" fill="var(--coral)"/></svg>Sociologists use a mixture of quantitative and qualitative methods to understand their areas of study.</li>
    <li><svg viewBox="0 0 22 22" aria-hidden="true"><circle cx="11" cy="11" r="7" fill="none" stroke="var(--coral)" stroke-width="4" stroke-dasharray="3 2.5"/><circle cx="11" cy="11" r="3" fill="var(--coral)"/></svg>Quantitative are a set of mathematical models or tools used to chart certain levels of social relations with high levels of certainty.</li>
    <li><svg viewBox="0 0 22 22" aria-hidden="true"><circle cx="11" cy="11" r="7" fill="none" stroke="var(--coral)" stroke-width="4" stroke-dasharray="3 2.5"/><circle cx="11" cy="11" r="3" fill="var(--coral)"/></svg>Qualitative are the close to close, subjective understandings of different social situations.</li>
    <li><svg viewBox="0 0 22 22" aria-hidden="true"><circle cx="11" cy="11" r="7" fill="none" stroke="var(--coral)" stroke-width="4" stroke-dasharray="3 2.5"/><circle cx="11" cy="11" r="3" fill="var(--coral)"/></svg>Sociologists may study it at the micro or macro levels.</li>
    <li><svg viewBox="0 0 22 22" aria-hidden="true"><circle cx="11" cy="11" r="7" fill="none" stroke="var(--coral)" stroke-width="4" stroke-dasharray="3 2.5"/><circle cx="11" cy="11" r="3" fill="var(--coral)"/></svg>Micro meaning, from 1 person to a group of people.</li>
    <li><svg viewBox="0 0 22 22" aria-hidden="true"><circle cx="11" cy="11" r="7" fill="none" stroke="var(--coral)" stroke-width="4" stroke-dasharray="3 2.5"/><circle cx="11" cy="11" r="3" fill="var(--coral)"/></svg>Macro meaning, on a regional to worldwide scale.</li>
  </ul>

  <div class="brain-figure" role="img" aria-label="Outline drawing of a human brain in coral"></div>

  <h2 class="section-title" style="top:978px">
    <svg viewBox="0 0 34 34" aria-hidden="true"><path d="M3 4h28v20H14l-8 7v-7H3z" fill="var(--teal)"/></svg>
    What do Sociologists study?
  </h2>
  <p class="study-intro">Some areas Sociologists study include:</p>

  <svg class="study-line" width="900" height="110" viewBox="0 0 900 110" aria-hidden="true">
    <g fill="var(--coral)">
      <circle cx="140" cy="26" r="8"/><circle cx="275" cy="26" r="8"/><circle cx="425" cy="26" r="8"/><circle cx="575" cy="26" r="8"/><circle cx="740" cy="26" r="8"/>
      <circle cx="200" cy="98" r="8"/><circle cx="345" cy="98" r="8"/><circle cx="495" cy="98" r="8"/><circle cx="640" cy="98" r="8"/><circle cx="780" cy="98" r="8"/>
    </g>
    <line x1="100" y1="82" x2="860" y2="82" stroke="var(--ink)" stroke-width="2"/>
    <g fill="var(--paper-bottom)" stroke="var(--ink)" stroke-width="2">
      <circle cx="140" cy="82" r="4"/><circle cx="200" cy="82" r="4"/><circle cx="275" cy="82" r="4"/><circle cx="345" cy="82" r="4"/><circle cx="425" cy="82" r="4"/><circle cx="495" cy="82" r="4"/><circle cx="575" cy="82" r="4"/><circle cx="640" cy="82" r="4"/><circle cx="740" cy="82" r="4"/><circle cx="780" cy="82" r="4"/>
    </g>
  </svg>

  <div class="topic upper" style="left:70px">The Family</div>
  <div class="topic upper" style="left:205px">Gender<br>Relations</div>
  <div class="topic upper" style="left:355px">Work</div>
  <div class="topic upper" style="left:505px">Race and<br>Ethnicity</div>
  <div class="topic upper" style="left:670px">Politics</div>

  <div class="topic lower" style="left:130px">Culture</div>
  <div class="topic lower" style="left:275px">Social Change<br>Movements</div>
  <div class="topic lower" style="left:425px">Sexuality</div>
  <div class="topic lower" style="left:570px">Death</div>
  <div class="topic lower" style="left:710px">Aging</div>
</main>
</body>
</html>
```